Barricade cover design needed for amusement ride exhibit

BrightPlayco is a company that sells coin operated amusement rides for kids that look and function like construction equipment such as excavator diggers and cranes. We need a design for vinyl covers that go over steel barricade fences formed around our amusement ride booth. The amusement ride booth is called "Tiny Gravel Corner" and is meant to look like a construction site where the machines are used. The design should incorporate things related to the construction industry but also be geared towards kids, toys, and fun!

Target Market(s)

Kids and Families

Industry/Entity Type

Amusement Park

Colors
fbed22
ffc214
fece3e
faa54b
f78f20

Requirements
Must have
• "Tiny Gravel Corner", "Powered By BrightPlayco"
Nice to have
• Male and Female Construction Characters, Caution Tape, Construction Signs

```html
<!DOCTYPE html>
<html lang="en">
<head>
<meta charset="utf-8">
<title>Tiny Gravel Corner – Barricade Cover</title>
<link href="https://fonts.googleapis.com/css2?family=Russo+One&display=swap" rel="stylesheet">
<style>
  :root {
    --page: #e9e9e6;
    --frame: #2b2c2e;
    --frame-edge: #1a1a1b;
    --panel: #0c0c0c;
    --hazard-yellow: #fbed22;
    --hazard-deep: #ffc214;
    --title-orange: #f15a24;
    --sponsor-bg: #b8a73a;
    --sponsor-ink: #141414;
    --steel-light: #e4e6e8;
    --steel-mid: #b9bcc0;
    --steel-dark: #8d9196;
    --figure-orange: #f78f20;
    --figure-blue: #2f6f9e;
    --cloud-grey: #8a8a8a;
  }
  * { margin: 0; padding: 0; box-sizing: border-box; }
  html, body { width: 1200px; height: 800px; overflow: hidden; background: var(--page); }

  .cover {
    position: absolute; left: 40px; top: 181px;
    width: 1120px; height: 438px;
    background: var(--frame);
    border: 2px solid var(--frame-edge);
    border-radius: 40px 40px 0 0;
  }
  .cover__panel {
    position: absolute; left: 37px; top: 30px;
    width: 1043px; height: 383px;
    background: var(--panel);
    border-radius: 14px;
    overflow: hidden;
  }
  .hazard-band {
    position: absolute; left: 0; width: 100%;
    background: repeating-linear-gradient(
      -56deg,
      var(--hazard-yellow) 0 38px,
      var(--panel) 38px 76px
    );
  }
  .hazard-band--top { top: 0; height: 110px; }
  .hazard-band--bottom { bottom: 0; height: 107px; }

  .title {
    position: absolute; left: 245px; top: 130px; width: 540px;
    font-family: "Russo One", sans-serif;
    color: var(--title-orange);
    text-align: center;
    text-transform: uppercase;
    line-height: 1.12;
    font-size: 54px;
    letter-spacing: 1px;
  }

  .sponsor {
    position: absolute; left: 810px; top: 147px;
    width: 222px; height: 92px;
    background: var(--sponsor-bg);
    clip-path: polygon(0 0, 100% 0, 100% 100%, 0 100%, 12px 50%);
    display: flex; flex-direction: column; justify-content: center; align-items: center;
    font-family: "Russo One", sans-serif;
    color: var(--sponsor-ink);
  }
  .sponsor__label { font-size: 13px; align-self: flex-end; margin-right: 38px; }
  .sponsor__name { font-size: 26px; }

  .figure { position: absolute; border-radius: 10px; }
  .figure--driller {
    left: 55px; top: 158px; width: 180px; height: 233px;
    background: linear-gradient(180deg, var(--figure-orange), var(--figure-blue) 60%, #8a6a44);
  }
  .figure--flagger {
    left: 240px; top: 225px; width: 150px; height: 173px;
    background: linear-gradient(180deg, var(--figure-orange), var(--figure-blue));
  }
  .figure--painter {
    left: 671px; top: 232px; width: 177px; height: 162px;
    background: linear-gradient(180deg, var(--cloud-grey), var(--figure-orange) 45%, var(--figure-blue));
  }

  .plate { position: absolute; left: 380px; width: 361px; }
  .plate--top { top: 0; height: 85px; }
  .plate--bottom { top: 361px; height: 77px; }
</style>
</head>
<body>
  <div class="cover">
    <div class="cover__panel">
      <div class="hazard-band hazard-band--top"></div>
      <div class="hazard-band hazard-band--bottom"></div>

      <div class="figure figure--driller" role="img" aria-label="Cartoon child construction worker in hard hat and goggles using a jackhammer on dirt"></div>
      <div class="figure figure--flagger" role="img" aria-label="Cartoon child construction worker waving beside a striped barrier"></div>
      <div class="figure figure--painter" role="img" aria-label="Cartoon child worker painting a grey cloud with a paint bucket at feet"></div>

      <h1 class="title">Tiny Gravel<br>Corner</h1>

      <div class="sponsor">
        <span class="sponsor__label">Powered By:</span>
        <span class="sponsor__name">BrightPlayco</span>
      </div>
    </div>

    <svg class="plate plate--top" viewBox="0 0 361 85" aria-hidden="true">
      <defs>
        <linearGradient id="steel-top" x1="0" y1="0" x2="0" y2="1">
          <stop offset="0" stop-color="var(--steel-light)"/>
          <stop offset="0.6" stop-color="var(--steel-mid)"/>
          <stop offset="1" stop-color="var(--steel-dark)"/>
        </linearGradient>
      </defs>
      <path d="M0 0 H361 L345 72 Q342 85 328 85 H33 Q19 85 16 72 Z" fill="url(#steel-top)"/>
      <polygon points="50,42 58,37 66,42 66,51 58,56 50,51" fill="#9aa0a6" stroke="#6e7379" stroke-width="2"/>
      <polygon points="295,42 303,37 311,42 311,51 303,56 295,51" fill="#9aa0a6" stroke="#6e7379" stroke-width="2"/>
    </svg>

    <svg class="plate plate--bottom" viewBox="0 0 361 77" aria-hidden="true">
      <defs>
        <linearGradient id="steel-bottom" x1="0" y1="0" x2="0" y2="1">
          <stop offset="0" stop-color="var(--steel-light)"/>
          <stop offset="0.6" stop-color="var(--steel-mid)"/>
          <stop offset="1" stop-color="var(--steel-dark)"/>
        </linearGradient>
      </defs>
      <path d="M16 12 Q19 0 33 0 H328 Q342 0 345 12 L358 77 H0 Z" fill="url(#steel-bottom)"/>
      <polygon points="50,22 58,17 66,22 66,31 58,36 50,31" fill="#9aa0a6" stroke="#6e7379" stroke-width="2"/>
      <polygon points="295,22 303,17 311,22 311,31 303,36 295,31" fill="#9aa0a6" stroke="#6e7379" stroke-width="2"/>
    </svg>
  </div>
</body>
</html>
```